Aerospace Private Equity Firm Needs Website

We need a website for new private equity fund called Corvin Partners. We buy smaller companies in the aerospace and industrial industries. I have attached some information about the firm. An example of a site we like that is a similar business but focused in a different sector is www.tarnowcare.com. www.quillstonefunds.com is a firm that also invests in aerospace companies.

Industry/Entity Type

Equity

Number of Pages Required

1 page

Colors
0555a3
33a6d7
ec1f27

```html
<!DOCTYPE html>
<html lang="en">
<head>
<meta charset="utf-8">
<title>Corvin Partners</title>
<link href="https://fonts.googleapis.com/css2?family=Open+Sans:wght@400;600;700&display=swap" rel="stylesheet">
<style>
:root{
  --blue:#0555a3;
  --navy:#0b3a83;
  --sky:#33a6d7;
  --red:#c8102e;
  --red-bright:#ec1f27;
  --ink:#222;
  --text:#555;
  --muted:#777;
  --dark-band:#454545;
  --footer-bg:#e9edf2;
  --white:#fff;
}
*{box-sizing:border-box;margin:0;padding:0}
html,body{width:1200px;height:2579px;overflow:hidden;background:var(--white)}
body{position:relative;font-family:"Open Sans",Arial,sans-serif;color:var(--ink)}
.abs{position:absolute}

/* header */
.site-header{left:0;top:0;width:1200px;height:122px;border-top:4px solid var(--navy);border-bottom:3px solid var(--red);background:var(--white)}
.brand{left:91px;top:28px;font-size:36px;font-weight:700;color:var(--navy);letter-spacing:-.5px;line-height:1}
.brand.footer-brand{left:0;width:1200px;text-align:center;top:2352px;font-size:38px}
.main-nav{top:44px;left:0;width:1200px;height:34px}
.main-nav a{position:absolute;top:0;height:34px;line-height:34px;font-size:18px;color:var(--ink);text-decoration:none;white-space:nowrap}
.main-nav a.active{background:var(--navy);color:var(--white);border-radius:17px;padding:0 19px;left:465px}

/* hero */
.hero{left:0;top:124px;width:1200px;height:580px;background:linear-gradient(100deg,#e3ecf4 0%,#cfdbe7 30%,#8a9bb2 55%,#34435c 75%,#1f2c44 100%)}
.hero-title{left:0;width:818px;text-align:center;top:318px;font-size:62px;font-weight:600;letter-spacing:1px;color:var(--navy);line-height:1}
.hero-title span{color:var(--red)}
.hero-sub{left:0;width:818px;text-align:center;top:393px;font-size:25px;color:#222}
.slider-btn{top:372px;width:26px;height:26px;border-radius:50%;background:rgba(40,40,40,.75)}
.slider-btn svg{display:block}
.hero-curve{left:0;top:600px;width:1200px;height:110px}

/* welcome */
.section-title{left:0;width:1200px;text-align:center;font-size:34px;font-weight:400;color:var(--ink)}
.welcome-text{left:155px;width:890px;top:814px;font-size:15.5px;line-height:26px;color:var(--text);text-align:justify}
.feature{width:300px;text-align:center}
.feature-icon{margin:0 auto;width:116px;height:116px;border-radius:50%;background:var(--navy);border:4px solid var(--white);box-shadow:0 0 0 2px var(--navy);display:flex;align-items:center;justify-content:center}
.feature h3{margin-top:24px;font-size:22px;font-weight:400;color:var(--ink)}
.feature p{margin:10px auto 0;width:260px;font-size:14.5px;line-height:23px;color:var(--muted)}
.feature .more{display:block;margin-top:8px;font-size:13.5px;color:var(--ink)}

/* key factors */
.factors-band{left:0;top:1284px;width:1200px;height:250px;background:linear-gradient(90deg,#3e3e3e,#5a5a5a 60%,#444)}
.factors-card{left:151px;top:1380px;width:898px;height:328px;background:var(--white);box-shadow:0 6px 24px rgba(0,0,0,.18);display:flex}
.factors-copy{width:497px;padding:40px 40px 0 40px}
.factors-copy h2{font-size:30px;font-weight:400;color:var(--ink);margin-bottom:6px}
.factors-copy p{font-size:14.5px;line-height:22px;color:#333;text-align:justify}
.btn-red{display:inline-block;margin-top:28px;width:110px;height:34px;line-height:34px;border-radius:17px;background:var(--red);color:var(--white);font-size:12px;text-align:center;text-transform:uppercase}
.factors-media{position:relative;width:401px;height:328px;background:radial-gradient(circle at 45% 50%,#2f8fd8 0%,#124a8c 45%,#061a3a 100%)}
.play{position:absolute;left:170px;top:134px;width:60px;height:60px;border-radius:50%;background:rgba(20,20,20,.75)}

/* news */
.news-card{top:1924px;width:315px}
.news-media{width:315px;height:190px;border:2px solid #e4e4e4}
.news-date{left:2px;top:-16px;width:50px;text-align:center;color:var(--white)}
.news-date .dm{background:var(--navy);height:58px;padding-top:6px}
.news-date .d{font-size:22px;line-height:26px}
.news-date .m{font-size:11px;line-height:14px}
.news-date .y{background:#2b2b2b;height:40px;line-height:40px;font-size:15px}
.news-card h3{margin-top:16px;font-size:17px;font-weight:400;color:#333}
.news-card p{margin-top:10px;font-size:12.5px;line-height:20px;color:var(--muted)}
.news-card .more{display:block;margin-top:10px;font-size:12px;color:var(--red)}

/* footer */
.site-footer{left:0;top:2280px;width:1200px;height:299px}
.social{top:2441px;left:0;width:1200px;display:flex;justify-content:center;gap:16px}
.social span{width:38px;height:38px;border-radius:50%;background:var(--white);border:1px solid #d6d6d6}
.social span.on{background:var(--navy);border-color:var(--navy)}
.footer-rule{left:70px;top:2518px;width:1060px;height:1px;background:#d3d8df}
.copyright{left:0;width:1200px;top:2538px;text-align:center;font-size:12px;color:#333}
</style>
</head>
<body>

<header class="site-header abs">
  <div class="brand abs">Corvin Partners</div>
  <nav class="main-nav abs">
    <a class="active" href="#">Home</a>
    <a href="#" style="left:582px">About us</a>
    <a href="#" style="left:705px">Services</a>
    <a href="#" style="left:821px">Projects</a>
    <a href="#" style="left:937px">Blog</a>
    <a href="#" style="left:1023px">Contact us</a>
  </nav>
</header>

<section class="hero abs" role="img" aria-label="Two businessmen in suits reviewing work together in a bright office"></section>
<h1 class="hero-title abs">CORVIN <span>PARTNERS</span></h1>
<p class="hero-sub abs">The aerospace and industrial industries</p>
<div class="slider-btn abs" style="left:71px"><svg width="26" height="26" viewBox="0 0 26 26"><path d="M15 8l-5 5 5 5" stroke="#fff" stroke-width="2" fill="none"/></svg></div>
<div class="slider-btn abs" style="left:1106px"><svg width="26" height="26" viewBox="0 0 26 26"><path d="M11 8l5 5-5 5" stroke="#fff" stroke-width="2" fill="none"/></svg></div>
<svg class="hero-curve abs" viewBox="0 0 1200 110" preserveAspectRatio="none">
  <path d="M0 20 Q560 120 1200 0 L1200 110 L0 110 Z" fill="var(--red)"/>
  <path d="M0 32 Q560 138 1200 10 L1200 110 L0 110 Z" fill="#fff"/>
</svg>

<h2 class="section-title abs" style="top:757px">Welcome To Corvin Partners</h2>
<p class="welcome-text abs">Corvin Partners (“Corvin”) is a Los Angeles, California-based private equity firm formed in 2016 by Principals from Linden Grove Associates (LGA). Corvin focuses on lower middle-market control investments in aerospace and industrial companies based in North America. The Corvin team has invested successfully in these sectors over a 10- year period while at LGA.</p>

<div class="feature abs" style="left:132px;top:942px">
  <div class="feature-icon"><svg width="40" height="40" viewBox="0 0 40 40"><path d="M6 14h8a4 4 0 1 1 8 0h8v8a4 4 0 1 0 0 8v6H6v-8a4 4 0 1 0 0-8z" fill="#fff"/></svg></div>
  <h3>Strategy</h3>
  <p>Corvin will invest in undervalued aero-space and industrial companies.</p>
  <span class="more">Learn More -&gt;</span>
</div>
<div class="feature abs" style="left:441px;top:942px">
  <div class="feature-icon"><svg width="44" height="32" viewBox="0 0 44 32"><rect x="2" y="4" width="40" height="24" rx="2" fill="none" stroke="#fff" stroke-width="3"/><circle cx="22" cy="16" r="6" fill="#fff"/></svg></div>
  <h3>Investment Criteria</h3>
  <p>Corvin will invest in undervalued aero-space and industrial companies.</p>
  <span class="more">Learn More -&gt;</span>
</div>
<div class="feature abs" style="left:766px;top:942px">
  <div class="feature-icon"><svg width="46" height="34" viewBox="0 0 46 34"><rect x="7" y="3" width="32" height="22" rx="2" fill="none" stroke="#fff" stroke-width="3"/><path d="M2 29h42v2H2z" fill="#fff"/></svg></div>
  <h3>Performance</h3>
  <p>Corvin will invest in undervalued aero-space and industrial companies.</p>
  <span class="more">Learn More -&gt;</span>
</div>

<section class="factors-band abs" role="img" aria-label="Dimmed office background"></section>
<article class="factors-card abs">
  <div class="factors-copy">
    <h2>KEY FACTORS</h2>
    <p>Aerospace is a large, growing global market that has historically outperformed the Broad 500 Index.</p>
    <p>Corvin strategically positioned – deep relationships with key suppliers and OEMs (Aldren, Kestrel, Marlow, Teverin, Northvale Aero)</p>
    <p>Preferred partner with OEMs – facilitates introductions to potential investments</p>
    <span class="btn-red">Read More</span>
  </div>
  <div class="factors-media" role="img" aria-label="Video still of a businessman touching a glowing private equity interface">
    <div class="play"><svg width="60" height="60" viewBox="0 0 60 60"><path d="M24 18l18 12-18 12z" fill="#fff"/></svg></div>
  </div>
</article>

<h2 class="section-title abs" style="top:1830px">Latest News</h2>

<article class="news-card abs" style="left:89px">
  <div class="news-media" role="img" aria-label="Businessman with a private equity digital interface" style="background:linear-gradient(120deg,#cfdbe8,#7f9bbd 55%,#3c5f8e)"></div>
  <div class="news-date abs"><div class="dm"><div class="d">02</div><div class="m">JUN</div></div><div class="y">2017</div></div>
  <h3>Porro quisquam est</h3>
  <p>It has survived not only five centuries, but also the leap into electronic typesetting,</p>
  <span class="more">Read More »</span>
</article>
<article class="news-card abs" style="left:443px">
  <div class="news-media" role="img" aria-label="Glowing private equity globe held in a hand" style="background:radial-gradient(circle at 50% 50%,#3a8ad8,#0e2d66 60%,#06122c)"></div>
  <div class="news-date abs"><div class="dm"><div class="d">02</div><div class="m">JUN</div></div><div class="y">2017</div></div>
  <h3>Dolorem ipsum quia</h3>
  <p>It has survived not only five centuries, but also the leap into electronic typesetting, remaining</p>
  <span class="more">Read More »</span>
</article>
<article class="news-card abs" style="left:796px">
  <div class="news-media" role="img" aria-label="Alarm clock beside stacks of coins with growing seedlings" style="background:linear-gradient(120deg,#dbe6c5,#a7bf7e 50%,#7f8d4a)"></div>
  <div class="news-date abs"><div class="dm"><div class="d">02</div><div class="m">JUN</div></div><div class="y">2017</div></div>
  <h3>Neque porro quisquam</h3>
  <p>It has survived not only five centuries, but also the leap into electronic typesetting, remaining</p>
  <span class="more">Read More »</span>
</article>

<footer class="site-footer abs">
  <svg width="1200" height="299" viewBox="0 0 1200 299" role="img" aria-label="Faded city and businessman backdrop">
    <defs><linearGradient id="fbg" x1="0" y1="0" x2="1" y2="0"><stop offset="0" stop-color="#eef1f5"/><stop offset=".6" stop-color="#e2e8ef"/><stop offset="1" stop-color="#d6dee8"/></linearGradient></defs>
    <path d="M0 58 Q600 -10 1200 58 L1200 299 L0 299 Z" fill="var(--red)"/>
    <path d="M0 66 Q600 0 1200 66 L1200 299 L0 299 Z" fill="url(#fbg)"/>
  </svg>
</footer>
<div class="brand footer-brand abs">Corvin Partners</div>
<div class="social abs"><span class="on"></span><span></span><span></span><span></span><span></span><span></span></div>
<div class="footer-rule abs"></div>
<p class="copyright abs">Copyright © 2017 All Rights Reserved</p>

</body>
</html>
```